Android Payment Application UI Design

We require a UI/UX design for an existing Android card-based payment application.

We're looking to improve the look + feel of the existing app. What we're after:
- Colour palette options
- Fonts
- Icons

See attached document for existing screen types, icons, etc.

All resources provided must be royalty free.

It's to run on a specialised device, with 720 x 1280 pixel resolution, in portrait only (landscape not required).

Please provide mockup examples of the new screen layout applied to the existing screens in the document.

Target Market(s)

Retail business users

Font styles to use
Sans Serif

Colors

Designer to choose colors to be used in the design.

Requirements
Must have
• Looking for
• - modern design
• - simple colours, easy-to-read sans-serif fonts
• - cohesive, consistent design between screens

```html
<!DOCTYPE html>
<html lang="en">
<head>
<meta charset="utf-8">
<title>NovaPay Terminal Screens</title>
<link rel="stylesheet" href="https://fonts.googleapis.com/css2?family=Montserrat:wght@300;400;500;600;700;800&display=swap">
<style>
:root{
  --bg:#6862b0;
  --status:#1a8ee2;
  --screen:#f4f4f5;
  --panel:#ffffff;
  --ink:#1c1c1e;
  --muted:#777b80;
  --line:#7fcbe8;
  --pad:#1b1b1c;
  --key:#111112;
  --red:#ea3a3a;
  --orange-a:#f49a2e;
  --orange-b:#e0702a;
  --blue-a:#33d1ec;
  --blue-b:#2e5fdc;
  --brand:#1d63c9;
  --teal:#18b8c6;
}
*{box-sizing:border-box;margin:0;padding:0}
html,body{width:1200px;height:1200px;overflow:hidden}
body{background:var(--bg);font-family:"Montserrat",sans-serif;color:var(--ink);position:relative}

.screen{position:absolute;width:238px;height:513px;background:var(--screen);overflow:hidden}
.status{height:19px;background:var(--status);color:#fff;font-size:10px;font-weight:600;display:flex;align-items:center;padding:0 8px;gap:8px}
.status .sq{width:8px;height:8px;border:1.5px solid #fff;border-radius:2px}
.status .icons{margin-left:auto;display:flex;gap:4px;align-items:center}
.status .bar{width:14px;height:6px;background:#fff;border-radius:2px}
.status .dot{width:6px;height:6px;border-radius:50%;background:#fff}

.header{height:85px;background:#fafafa;display:flex;align-items:center;justify-content:center;box-shadow:0 4px 10px rgba(0,0,0,.04);position:relative}
.brand{display:flex;flex-direction:column;align-items:center}
.brand-row{display:flex;align-items:center;gap:5px}
.brand-mark{width:22px;height:22px;border-radius:50%;background:var(--brand)}
.brand-name{font-size:18px;font-weight:800;color:var(--brand);letter-spacing:1px}
.brand-tag{font-size:5.5px;font-weight:600;color:var(--ink);margin-top:2px}

.title{position:absolute;left:0;right:0;text-align:center;font-weight:800;font-size:21px}
.panel{position:absolute;background:var(--panel);border-radius:9px;box-shadow:0 4px 14px rgba(0,0,0,.06)}
.label{font-size:8.5px;font-weight:600;color:var(--muted);letter-spacing:.8px;text-align:center}
.field{position:absolute;border:1.5px solid var(--line);border-radius:5px;background:#fff}

.keypad{position:absolute;left:0;right:0;bottom:0;height:217px;background:var(--pad);padding:7px 7px 22px;display:grid;grid-template-columns:repeat(4,1fr);grid-template-rows:repeat(4,1fr);gap:2px}
.key{background:var(--key);color:#fff;display:flex;align-items:center;justify-content:center;font-size:15px;font-weight:300;border-radius:2px}
.key.blank{background:var(--pad)}
.key.cancel{background:var(--red);font-size:8px;font-weight:500;letter-spacing:.3px}
.key.back{background:linear-gradient(180deg,var(--orange-a),var(--orange-b))}
.key.done{grid-row:span 2;background:linear-gradient(160deg,var(--blue-a),var(--blue-b));flex-direction:column;gap:4px;font-size:8px;font-weight:500}

.splash{position:absolute;left:66px;top:38px;width:246px;height:534px;border-radius:30px;background:linear-gradient(160deg,#1f9cf0 0%,#0d7fe0 60%,#0a74d6 100%);color:#fff;overflow:hidden}
.splash .time{position:absolute;left:21px;top:11px;font-size:10px;font-weight:600}
.splash .notch{position:absolute;left:55px;top:0;width:136px;height:20px;background:var(--bg);border-radius:0 0 16px 16px}
.splash .brand{position:absolute;left:0;right:0;top:198px}
.splash .brand-mark{background:#fff;width:32px;height:32px}
.splash .brand-name{color:#fff;font-size:30px}
.splash .brand-tag{color:#fff;font-size:9px}
.splash .rule{position:absolute;left:16px;right:16px;top:447px;height:1px;background:rgba(255,255,255,.45)}
.splash .ver{position:absolute;left:0;right:0;top:460px;text-align:center;font-size:8px;font-weight:600;line-height:15px}
.splash .home{position:absolute;left:78px;bottom:10px;width:90px;height:3px;border-radius:2px;background:rgba(255,255,255,.8)}

.tabs{position:absolute;top:96px;left:6px;right:6px;display:flex;font-size:7.5px;font-weight:700;letter-spacing:.6px;height:16px}
.tabs span{flex:1;text-align:center}
.tabs .active{border-bottom:2px solid var(--status)}
.tabs .idle{color:#9a9ea3}
.menu-list{left:12px;top:123px;width:214px;padding:0 13px}
.menu-row{height:44px;display:flex;align-items:center;font-size:10.5px;font-weight:700;border-bottom:1px solid #e4e4e6}
.menu-row:last-child{border-bottom:none}
.menu-row svg{margin-left:auto}

.pin-row{position:absolute;top:224px;left:22px;display:flex;gap:8px}
.pin{width:43px;height:40px;border:1.5px solid var(--line);border-radius:3px;background:#fff;display:flex;align-items:center;justify-content:center;font-size:13px;font-weight:600}

.dots{position:absolute;top:121px;left:0;right:0;display:flex;justify-content:space-around;padding:0 20px}
.dots span{width:18px;height:18px;border-radius:50%}
.pay-card{position:absolute;left:27px;top:202px;width:184px;height:119px;border-radius:8px;background:linear-gradient(120deg,#2e6fe0,#3bcfe8);color:#fff;box-shadow:0 8px 18px rgba(0,0,0,.15)}
.pay-card .amt{position:absolute;left:40px;top:10px;font-size:24px;font-weight:700}
.pay-card .amt small{font-size:9px;font-weight:500}
.tap-text{position:absolute;top:354px;left:0;right:0;text-align:center;font-size:11px;line-height:15px;font-weight:500}
.scheme-row{position:absolute;top:438px;left:20px;right:20px;display:flex;justify-content:space-between;align-items:center;font-size:12px;font-weight:700;color:var(--brand)}
.scheme{display:flex;align-items:center;gap:4px}
.scheme i{width:12px;height:12px;border-radius:50%;background:var(--brand);display:block}
</style>
</head>
<body>

<div class="splash">
  <div class="notch"></div>
  <div class="time">9:41</div>
  <div class="brand">
    <div class="brand-row"><span class="brand-mark"></span><span class="brand-name">NOVA</span></div>
    <div class="brand-tag">Smart Payments, Simply Done</div>
  </div>
  <div class="rule"></div>
  <div class="ver">NovaPay, (0.0.1)<br>Nova UK Demo</div>
  <div class="home"></div>
</div>

<div class="screen" style="left:343px;top:63px">
  <div class="status"><span class="sq"></span>9:41<span class="icons"><span class="bar"></span><span class="dot"></span><span class="bar"></span></span></div>
  <div class="header"><div class="brand"><div class="brand-row"><span class="brand-mark"></span><span class="brand-name">NOVA</span></div><div class="brand-tag">Smart Payments, Simply Done</div></div></div>
  <div class="title" style="top:130px">Welcome</div>
  <div class="label" style="position:absolute;top:159px;left:0;right:0">Enter User Credentials</div>
  <div class="panel" style="left:12px;top:175px;width:214px;height:140px"></div>
  <div class="field" style="left:22px;top:193px;width:190px;height:32px"><span class="label" style="position:absolute;left:14px;top:11px">USER ID</span></div>
  <div class="field" style="left:22px;top:232px;width:190px;height:32px"><span class="label" style="position:absolute;left:14px;top:11px">Password</span></div>
  <div class="keypad">
    <div class="key">1</div><div class="key">2</div><div class="key">3</div><div class="key cancel">CANCEL</div>
    <div class="key">4</div><div class="key">5</div><div class="key">6</div><div class="key back"><svg width="18" height="12" viewBox="0 0 18 12"><path d="M5 1h12v10H5L1 6z" fill="none" stroke="#fff" stroke-width="1.5"/><path d="M8 4l4 4M12 4l-4 4" stroke="#fff" stroke-width="1.5"/></svg></div>
    <div class="key">7</div><div class="key">8</div><div class="key">9</div><div class="key done"><svg width="11" height="8" viewBox="0 0 11 8"><path d="M1 4l3 3 6-6" fill="none" stroke="#fff" stroke-width="1.3"/></svg>DONE</div>
    <div class="key">00</div><div class="key">0</div><div class="key">000</div>
  </div>
</div>

<div class="screen" style="left:619px;top:63px">
  <div class="status"><span class="sq"></span>9:41<span class="icons"><span class="bar"></span><span class="dot"></span><span class="bar"></span></span></div>
  <div class="header" style="height:110px;align-items:flex-start;padding-top:10px">
    <svg style="position:absolute;left:16px;top:23px" width="20" height="10" viewBox="0 0 20 10"><rect x="1" y="1" width="16" height="8" rx="1.5" fill="none" stroke="#ea3a3a" stroke-width="1.4"/><rect x="3" y="3" width="4" height="4" fill="#ea3a3a"/><rect x="17.5" y="3.5" width="2" height="3" fill="#ea3a3a"/></svg>
    <svg style="position:absolute;right:14px;top:25px" width="3" height="12" viewBox="0 0 3 12"><circle cx="1.5" cy="1.5" r="1.2" fill="#333"/><circle cx="1.5" cy="6" r="1.2" fill="#333"/><circle cx="1.5" cy="10.5" r="1.2" fill="#333"/></svg>
    <div class="brand"><div class="brand-row"><span class="brand-mark"></span><span class="brand-name">NOVA</span></div><div class="brand-tag">Smart Payments, Simply Done</div></div>
  </div>
  <div class="tabs"><span class="active">MAIN MENU</span><span class="idle">ADMINMENU</span></div>
  <div class="panel menu-list">
    <div class="menu-row">Sale<svg width="6" height="10" viewBox="0 0 6 10"><path d="M1 1l4 4-4 4" fill="none" stroke="#999" stroke-width="1.2"/></svg></div>
    <div class="menu-row">Reversal<svg width="6" height="10" viewBox="0 0 6 10"><path d="M1 1l4 4-4 4" fill="none" stroke="#999" stroke-width="1.2"/></svg></div>
    <div class="menu-row">Refund<svg width="6" height="10" viewBox="0 0 6 10"><path d="M1 1l4 4-4 4" fill="none" stroke="#999" stroke-width="1.2"/></svg></div>
    <div class="menu-row">Pre-Auth<svg width="6" height="10" viewBox="0 0 6 10"><path d="M1 1l4 4-4 4" fill="none" stroke="#999" stroke-width="1.2"/></svg></div>
    <div class="menu-row">Completion<svg width="6" height="10" viewBox="0 0 6 10"><path d="M1 1l4 4-4 4" fill="none" stroke="#999" stroke-width="1.2"/></svg></div>
    <div class="menu-row">Reconciliation<svg width="6" height="10" viewBox="0 0 6 10"><path d="M1 1l4 4-4 4" fill="none" stroke="#999" stroke-width="1.2"/></svg></div>
  </div>
</div>

<div class="screen" style="left:891px;top:63px">
  <div class="status"><span class="sq"></span>9:41<span class="icons"><span class="bar"></span><span class="dot"></span><span class="bar"></span></span></div>
  <div class="header"><div class="brand"><div class="brand-row"><span class="brand-mark"></span><span class="brand-name">NOVA</span></div><div class="brand-tag">Smart Payments, Simply Done</div></div></div>
  <div class="title" style="top:131px">SALE</div>
  <div class="panel" style="left:11px;top:181px;width:216px;height:130px"></div>
  <div class="label" style="position:absolute;top:199px;left:0;right:0">Enter Pin</div>
  <div class="pin-row"><div class="pin">1</div><div class="pin">1</div><div class="pin">1</div><div class="pin">1</div></div>
  <div class="keypad">
    <div class="key">1</div><div class="key">2</div><div class="key">3</div><div class="key cancel"><svg width="11" height="11" viewBox="0 0 11 11"><path d="M1 1l9 9M10 1l-9 9" stroke="#fff" stroke-width="2"/></svg></div>
    <div class="key">4</div><div class="key">5</div><div class="key">6</div><div class="key back"><svg width="18" height="12" viewBox="0 0 18 12"><path d="M5 1h12v10H5L1 6z" fill="none" stroke="#fff" stroke-width="1.5"/><path d="M8 4l4 4M12 4l-4 4" stroke="#fff" stroke-width="1.5"/></svg></div>
    <div class="key">7</div><div class="key">8</div><div class="key">9</div><div class="key done"><svg width="24" height="36" viewBox="0 0 24 36"><path d="M20 1v28H3M9 23l-6 6 6 6" fill="none" stroke="#fff" stroke-width="1.8"/></svg></div>
    <div class="key blank"></div><div class="key">0</div><div class="key blank"></div>
  </div>
</div>

<div class="screen" style="left:70px;top:618px">
  <div class="status"><span class="sq"></span>9:41<span class="icons"><span class="bar"></span><span class="dot"></span><span class="bar"></span></span></div>
  <div class="header"><div class="brand"><div class="brand-row"><span class="brand-mark"></span><span class="brand-name">NOVA</span></div><div class="brand-tag">Smart Payments, Simply Done</div></div></div>
  <div class="title" style="top:130px">SALE</div>
  <div class="panel" style="left:11px;top:181px;width:216px;height:130px"></div>
  <div class="label" style="position:absolute;top:200px;left:0;right:0">Please Enter Card Number</div>
  <div class="field" style="left:19px;top:222px;width:200px;height:41px"></div>
  <div class="keypad">
    <div class="key">1</div><div class="key">2</div><div class="key">3</div><div class="key cancel">CANCEL</div>
    <div class="key">4</div><div class="key">5</div><div class="key">6</div><div class="key back"><svg width="18" height="12" viewBox="0 0 18 12"><path d="M5 1h12v10H5L1 6z" fill="none" stroke="#fff" stroke-width="1.5"/><path d="M8 4l4 4M12 4l-4 4" stroke="#fff" stroke-width="1.5"/></svg></div>
    <div class="key">7</div><div class="key">8</div><div class="key">9</div><div class="key done"><svg width="11" height="8" viewBox="0 0 11 8"><path d="M1 4l3 3 6-6" fill="none" stroke="#fff" stroke-width="1.3"/></svg>DONE</div>
    <div class="key">00</div><div class="key">0</div><div class="key">000</div>
  </div>
</div>

<div class="screen" style="left:343px;top:618px">
  <div class="status"><span class="sq"></span>9:41<span class="icons"><span class="bar"></span><span class="dot"></span><span class="bar"></span></span></div>
  <div class="header"><div class="brand"><div class="brand-row"><span class="brand-mark"></span><span class="brand-name">NOVA</span></div><div class="brand-tag">Smart Payments, Simply Done</div></div></div>
  <div class="dots"><span style="background:#1a8ee2;box-shadow:0 0 0 4px #bfe1f7"></span><span style="background:#19d27a"></span><span style="background:#ef3a3a"></span><span style="background:#f7b24a"></span></div>
  <div class="title" style="top:154px">SALE</div>
  <div class="panel" style="left:12px;top:240px;width:214px;height:236px"></div>
  <div class="pay-card">
    <div class="amt"><small>GBP </small>2798<small>.34</small></div>
    <svg style="position:absolute;left:56px;top:50px" width="74" height="50" viewBox="0 0 74 50"><ellipse cx="34" cy="25" rx="32" ry="22" fill="none" stroke="#102a5a" stroke-width="1.5"/><path d="M20 19q3 6 0 12M25 16q5 9 0 18M30 13q7 12 0 24" fill="none" stroke="#102a5a" stroke-width="2"/><rect x="44" y="14" width="16" height="12" rx="2" transform="rotate(-15 52 20)" fill="none" stroke="#102a5a" stroke-width="1.5"/></svg>
  </div>
  <div class="tap-text">Please Tap<br>Swipe or Insert Card</div>
  <div style="position:absolute;top:414px;left:35px;right:38px;height:1px;background:#dcdcde"></div>
  <div class="scheme-row">
    <span class="scheme"><i></i>Veyra</span>
    <span class="scheme"><i></i>Tolvo</span>
    <span class="scheme"><i></i>Quenta</span>
  </div>
</div>

<div class="screen" style="left:618px;top:618px">
  <div class="status"><span class="sq"></span>9:41<span class="icons"><span class="bar"></span><span class="dot"></span><span class="bar"></span></span></div>
  <div class="header"><div class="brand"><div class="brand-row"><span class="brand-mark"></span><span class="brand-name">NOVA</span></div><div class="brand-tag">Smart Payments, Simply Done</div></div></div>
  <div class="title" style="top:131px">SALE</div>
  <div class="panel" style="left:11px;top:182px;width:216px;height:130px"></div>
  <div class="label" style="position:absolute;top:200px;left:0;right:0">Please Enter amount</div>
  <div class="field" style="left:19px;top:223px;width:200px;height:41px;display:flex;align-items:center">
    <span style="flex:1;text-align:center;font-size:13px;font-weight:600;letter-spacing:1px;padding-left:12px">0.00</span>
    <span style="border-left:1px solid #ddd;height:22px;padding:4px 12px;font-size:11px;font-weight:600;color:#666;letter-spacing:1px">GBP</span>
  </div>
  <div class="keypad">
    <div class="key">1</div><div class="key">2</div><div class="key">3</div><div class="key cancel">CANCEL</div>
    <div class="key">4</div><div class="key">5</div><div class="key">6</div><div class="key back"><svg width="18" height="12" viewBox="0 0 18 12"><path d="M5 1h12v10H5L1 6z" fill="none" stroke="#fff" stroke-width="1.5"/><path d="M8 4l4 4M12 4l-4 4" stroke="#fff" stroke-width="1.5"/></svg></div>
    <div class="key">7</div><div class="key">8</div><div class="key">9</div><div class="key done"><svg width="11" height="8" viewBox="0 0 11 8"><path d="M1 4l3 3 6-6" fill="none" stroke="#fff" stroke-width="1.3"/></svg>DONE</div>
    <div class="key">00</div><div class="key">0</div><div class="key">000</div>
  </div>
</div>

<div class="screen" style="left:891px;top:618px">
  <div class="status"><span class="sq"></span>9:41<span class="icons"><span class="bar"></span><span class="dot"></span><span class="bar"></span></span></div>
  <div class="header"><div class="brand"><div class="brand-row"><span class="brand-mark"></span><span class="brand-name">NOVA</span></div><div class="brand-tag">Smart Payments, Simply Done</div></div></div>
  <div class="title" style="top:133px;font-size:17.5px">TEST CONNECT</div>
  <div class="panel" style="left:11px;top:171px;width:216px;height:155px"></div>
  <div style="position:absolute;top:206px;left:0;right:0;text-align:center;color:var(--teal);font-size:16px;font-weight:600">Autorised</div>
  <svg style="position:absolute;left:101px;top:242px" width="36" height="36" viewBox="0 0 36 36"><circle cx="18" cy="18" r="18" fill="#1aa9dc"/><path d="M10 18l6 6 11-12" fill="none" stroke="#fff" stroke-width="3.2" stroke-linecap="round" stroke-linejoin="round"/></svg>
</div>

</body>
</html>
```